we can communicate on this, but i want to follow the approach we took on Pell|Quorn & Tillet but i feel the card front needs the black background and the platinum and gold logo. The back? I am open. we can use the same info from PQ&T. Vellum Crest is an enhanced equity investment fund - basically a very exclusive boutique hedge fund that uses only stock options. very advanced things. hope you are interested

Contact Information for Business Card

Dr. Owen T. Brisket, CFA
Scientifique de fusée financière
555.014.2296
TheDoc4793@mailvessel.example

4718 Fennel Brook Way N.
West Fargo, ND 58078

No web site

Colors

Designer to choose colors to be used in the design.

Requirements
Nice to have
• I tend to prefer the most visible applications of the logo to include logo and name, the logo version with a black background and the gold and platinum components separated by the black. I see this working well for a single side (logo and name - this is card front to me).
• I am fairly open to other treatments on the reverse side with the data. To me, it makes sense to have a different color rendition of the logo on the reverse and it may be a muted black tone on tone or an oversized portion that would have spot UV. Or, the reverse may play with colors and layout
Should not have
• Other colors = no no
• Decorative font

```html
<!DOCTYPE html>
<html lang="en">
<head>
<meta charset="utf-8">
<title>Vellum Crest — Business Card</title>
<link rel="stylesheet" href="https://fonts.googleapis.com/css2?family=Open+Sans:wght@400;600;700&family=Roboto:wght@400&display=swap">
<style>
  :root {
    --canvas: #2b2b2b;
    --card: #161616;
    --gold: #c9a544;
    --white: #ffffff;
    --text: #f2f2f2;
  }
  * { margin: 0; padding: 0; box-sizing: border-box; }
  html, body {
    width: 1200px; height: 900px; overflow: hidden;
    background: var(--canvas);
  }
  .canvas { position: relative; width: 1200px; height: 900px; }
  .card {
    position: absolute; left: 290px; width: 620px; height: 354px;
    background: var(--card); border-radius: 22px;
    box-shadow: 0 12px 30px rgba(0,0,0,0.45);
    overflow: hidden;
  }
  .card--front { top: 60px; }
  .card--back { top: 486px; }

  .brand {
    position: absolute; display: flex; flex-direction: column; align-items: center;
    font-family: "Open Sans", sans-serif; font-weight: 700; color: var(--white);
  }
  .brand__mark {
    width: 92px; height: 92px; border-radius: 50%; background: var(--gold);
    margin-bottom: 16px;
  }
  .brand__name {
    font-size: 40px; letter-spacing: 2px; text-transform: uppercase; line-height: 1;
    white-space: nowrap;
  }
  .card--front .brand { left: 0; right: 0; top: 90px; }
  .card--back .brand { left: 28px; width: 270px; top: 100px; }
  .card--back .brand__mark { width: 84px; height: 84px; }
  .card--back .brand__name { font-size: 30px; }

  .contact {
    position: absolute; left: 318px; top: 86px; width: 284px;
    font-family: "Roboto", sans-serif; color: var(--text);
  }
  .contact__name {
    font-family: "Open Sans", sans-serif; font-weight: 700; font-size: 17px;
    color: var(--gold); letter-spacing: 1px; text-transform: uppercase; line-height: 1.2;
    white-space: nowrap;
  }
  .contact__role {
    font-family: "Open Sans", sans-serif; font-weight: 600; font-size: 15px;
    color: var(--white); margin-bottom: 18px; white-space: nowrap;
  }
  .contact__address { font-size: 14px; line-height: 1.4; margin-bottom: 16px; }
  .contact__list { list-style: none; font-size: 14px; }
  .contact__item { display: flex; align-items: center; gap: 10px; margin-bottom: 6px; white-space: nowrap; }
  .contact__icon { width: 13px; height: 13px; flex: none; }
</style>
</head>
<body>
<main class="canvas">
  <section class="card card--front" aria-label="Card front">
    <div class="brand">
      <span class="brand__mark" aria-hidden="true"></span>
      <span class="brand__name">Vellum Crest</span>
    </div>
  </section>

  <section class="card card--back" aria-label="Card back">
    <div class="brand">
      <span class="brand__mark" aria-hidden="true"></span>
      <span class="brand__name">Vellum Crest</span>
    </div>
    <div class="contact">
      <h1 class="contact__name">Dr. Owen T. Brisket, CFA</h1>
      <p class="contact__role">Scientifique de fusée financière</p>
      <p class="contact__address">4718 Fennel Brook Way N.<br>West Fargo, ND 58078</p>
      <ul class="contact__list">
        <li class="contact__item">
          <svg class="contact__icon" viewBox="0 0 24 24" aria-hidden="true"><path fill="#c9a544" d="M6.6 10.8a15 15 0 0 0 6.6 6.6l2.2-2.2c.3-.3.7-.4 1-.2 1.1.4 2.3.6 3.6.6.6 0 1 .4 1 1V20c0 .6-.4 1-1 1C10.6 21 3 13.4 3 4c0-.6.4-1 1-1h3.5c.6 0 1 .4 1 1 0 1.3.2 2.5.6 3.6.1.3 0 .7-.2 1l-2.3 2.2z"/></svg>
          <span>555.014.2296</span>
        </li>
        <li class="contact__item">
          <svg class="contact__icon" viewBox="0 0 24 24" aria-hidden="true"><rect x="2" y="5" width="20" height="14" rx="1.5" fill="none" stroke="#c9a544" stroke-width="2.4"/><path d="M3 6l9 7 9-7" fill="none" stroke="#c9a544" stroke-width="2.4"/></svg>
          <span>TheDoc4793@mailvessel.example</span>
        </li>
      </ul>
    </div>
  </section>
</main>
</body>
</html>
```